Tidy fern Services

After a high quality design website. we are a company that provides services to people that own land and need a hand getting on top of the delayed jobs.
would want a number of tab/ pages for the web page.
Home page / About us page / services page / Gallery page. / Contact us page
we offer a wide range of services .listed below

Stock Work (title)

Stock movement
Break feeding
Temporary staffing

Spraying (title)

Spraying weeds
Spraying gorse

Pastures (title)

Fertilizing
Topping

Building (title)

Habitable sheds
Farm sheds
Sheep yards
Cattle yards
Repair farm buildings
Decks
Retaining walls

Fencing (title)

Stock fencing
Post & rail
Stock yards repair
Electric fencing install & repairs

Water Management (title)

Water trough installation
Water scheme install
Water trough cleaning
Farm water maintenance
Water ponds
Ornamental ponds
Drainage

General (title)

Lawn mowing
Hedge trimming
Pruning trees
Metaling drive ways & races
Water blasting
Small digger work
Little tip truck cartage
Home kill management
Mulching gorse
Section clearing

```html
<!DOCTYPE html>
<html lang="en">
<head>
<meta charset="utf-8">
<title>Tidy fern Services</title>
<link href="https://fonts.googleapis.com/css2?family=Lexend:wght@300;400&family=Poppins:wght@400;500;600;700&display=swap" rel="stylesheet">
<style>
:root{
  --green:#5a9414;
  --green-dark:#3f700a;
  --green-light:#8cc63f;
  --ink:#111111;
  --text:#222222;
  --white:#ffffff;
}
*{box-sizing:border-box;margin:0;padding:0}
html,body{width:1200px;height:4060px;overflow:hidden;background:var(--white)}
body{position:relative;font-family:"Poppins",sans-serif;color:var(--text)}
.abs{position:absolute}
.topline{left:0;top:0;width:1200px;height:4px;background:var(--green)}
.phone-pill{left:702px;top:0;width:340px;height:44px;background:var(--green);border-radius:0 0 170px 170px/0 0 44px 44px;color:var(--white);font-weight:600;font-size:19px;display:flex;align-items:center;justify-content:center;gap:10px}
.phone-pill svg{width:22px;height:22px}
.brand{display:flex;align-items:center;gap:12px;color:var(--green);font-weight:600;line-height:1;text-decoration:none}
.brand .mark{border:3px solid var(--green);border-radius:50%}
.brand .name{display:flex;flex-direction:column}
.brand .name small{letter-spacing:4px;margin-top:6px}
.header-brand{left:145px;top:20px}
.header-brand .mark{width:84px;height:84px}
.header-brand .name{font-size:30px}
.header-brand .name small{font-size:16px}
.nav{font-weight:600;font-size:14px;color:var(--ink)}
.nav a{position:absolute;white-space:nowrap;color:var(--ink);text-decoration:none}
.main-nav{top:68px;left:576px}
.main-nav a.active::before{content:"";position:absolute;left:-2px;right:-2px;top:-8px;height:8px;border-top:2px solid var(--green);border-radius:50% 50% 0 0}
.hero-badge{left:155px;top:216px;width:432px;height:432px;border-radius:50%;background:var(--green);color:var(--white);text-align:center;display:flex;flex-direction:column;align-items:center;justify-content:center}
.hero-badge h1{font-family:"Lexend",sans-serif;font-weight:300;font-size:52px;line-height:1.15}
.hero-badge p{font-weight:600;font-size:17px;line-height:1.4;margin:24px 40px 22px}
.btn{display:inline-flex;align-items:center;justify-content:center;border-radius:30px;font-weight:700;font-size:15px;text-decoration:none}
.btn-white{background:var(--white);color:var(--ink);width:148px;height:54px}
.btn-green{background:var(--green);color:var(--white);width:148px;height:54px}
.btn-black{background:var(--ink);color:var(--white);width:148px;height:56px}
.dots{left:1105px;top:398px;display:flex;flex-direction:column;gap:8px}
.dots i{width:9px;height:9px;border-radius:50%;background:var(--white)}
.dots i.on{background:var(--green-light)}
.section-title{width:1200px;left:0;text-align:center;font-family:"Lexend",sans-serif;font-weight:300;font-size:50px;color:var(--ink)}
.service{width:300px;text-align:center}
.service .ring{width:288px;height:288px;margin:0 auto;border-radius:50%;border:7px solid var(--ink);border-left-color:var(--green);border-bottom-color:var(--green);padding:10px;transform:rotate(-20deg)}
.service .photo{width:100%;height:100%;border-radius:50%;transform:rotate(20deg)}
.service h3{font-size:18px;font-weight:600;color:var(--ink);margin-top:22px;line-height:1.35}
.spray-overlay{left:513px;top:1003px;width:172px;height:172px;border-radius:50%;background:rgba(90,148,20,.92);border:4px solid var(--white);color:var(--white);text-align:center;display:flex;flex-direction:column;justify-content:center}
.spray-overlay strong{font-size:18px;font-weight:600;margin-bottom:10px}
.spray-overlay span{font-size:12px;line-height:1.5}
.about-photo{left:145px;top:1924px;width:340px;height:340px;border-radius:50%}
.about-copy{left:555px;top:1905px;width:500px;color:var(--white)}
.about-copy h2{font-family:"Lexend",sans-serif;font-weight:300;font-size:52px;margin-bottom:20px}
.about-copy p{font-size:13px;line-height:25.6px;text-align:justify;margin-bottom:26px}
.gallery{left:144px;top:2559px;width:911px;display:grid;grid-template-columns:repeat(3,1fr);gap:9px}
.gallery div{height:261px}
.zoom{left:584px;top:2677px;width:30px;height:30px;border-radius:50%;background:var(--green);display:flex;align-items:center;justify-content:center}
.contact-title{top:3392px;color:var(--white)}
.field{background:var(--white);border-radius:24px;font-size:12px;color:#444;padding:0 28px;display:flex;align-items:center}
.field.msg{align-items:flex-start;padding-top:16px;border-radius:22px}
.footer-brand{left:145px;top:3903px}
.footer-brand .mark{width:96px;height:96px}
.footer-brand .name{font-size:34px}
.footer-brand .name small{font-size:19px}
.footer-nav{top:3926px;left:574px}
.copyright{left:574px;top:3960px;font-size:13px;color:#333}
.socials{left:576px;top:3998px;display:flex;gap:7px}
.socials i{width:24px;height:24px;border-radius:50%;border:2px solid var(--green)}
</style>
</head>
<body>
<div class="abs topline"></div>
<div class="abs phone-pill">
  <svg viewBox="0 0 24 24"><circle cx="12" cy="12" r="12" fill="#fff"/><path d="M8.2 6.5l1.6-.4 1.2 2.8-1.2 1c.6 1.4 1.6 2.5 3 3.2l1-1.2 2.8 1.2-.4 1.7c-.2.6-.8.9-1.4.8-3.6-.6-6.9-3.8-7.4-7.5-.1-.6.2-1.2.8-1.6z" fill="#5a9414"/></svg>
  +1 555 010 2040
</div>

<a class="abs brand header-brand"><span class="mark"></span><span class="name">TIDY FERN<small>SERVICES</small></span></a>

<nav class="abs nav main-nav">
  <a class="active" style="left:0">HOME</a>
  <a style="left:80px">ABOUT US</a>
  <a style="left:187px">SERVICES</a>
  <a style="left:291px">GALLERY</a>
  <a style="left:389px">CONTACT US</a>
</nav>

<svg class="abs" style="left:0;top:100px" width="1200" height="670" viewBox="0 100 1200 670">
  <defs>
    <clipPath id="heroClip"><ellipse cx="600" cy="432" rx="580" ry="316"/></clipPath>
    <linearGradient id="heroBase" x1="0" y1="0" x2="0" y2="1">
      <stop offset="0" stop-color="#557a2c"/>
      <stop offset=".45" stop-color="#3c5f23"/>
      <stop offset=".7" stop-color="#243b1c"/>
      <stop offset="1" stop-color="#16241a"/>
    </linearGradient>
    <radialGradient id="heroBokeh" cx=".5" cy=".5" r=".5">
      <stop offset="0" stop-color="#c9dd8a" stop-opacity=".85"/>
      <stop offset="1" stop-color="#c9dd8a" stop-opacity="0"/>
    </radialGradient>
    <radialGradient id="heroDrop" cx=".5" cy=".5" r=".5">
      <stop offset="0" stop-color="#d7ecd9" stop-opacity=".95"/>
      <stop offset=".45" stop-color="#7fb04a" stop-opacity=".8"/>
      <stop offset="1" stop-color="#7fb04a" stop-opacity="0"/>
    </radialGradient>
    <radialGradient id="heroWater" cx=".5" cy=".5" r=".5">
      <stop offset="0" stop-color="#6f8a7e" stop-opacity=".7"/>
      <stop offset="1" stop-color="#6f8a7e" stop-opacity="0"/>
    </radialGradient>
  </defs>
  <ellipse cx="606" cy="440" rx="590" ry="320" fill="var(--ink)"/>
  <ellipse cx="594" cy="428" rx="590" ry="320" fill="var(--green)"/>
  <g clip-path="url(#heroClip)" role="img" aria-label="Forest stream with a water droplet holding a small green world">
    <rect x="0" y="100" width="1200" height="670" fill="url(#heroBase)"/>
    <ellipse cx="230" cy="220" rx="260" ry="170" fill="url(#heroBokeh)"/>
    <ellipse cx="980" cy="230" rx="230" ry="150" fill="url(#heroBokeh)" opacity=".6"/>
    <ellipse cx="560" cy="170" rx="180" ry="110" fill="url(#heroBokeh)" opacity=".5"/>
    <ellipse cx="745" cy="470" rx="140" ry="160" fill="url(#heroDrop)"/>
    <ellipse cx="700" cy="640" rx="420" ry="90" fill="url(#heroWater)"/>
  </g>
</svg>

<div class="abs hero-badge">
  <h1>TIDY FERN<br>SERVICES</h1>
  <p>Sed ut perspiciatis unde omnis iste natus error sit voluptatem</p>
  <a class="btn btn-white">GET STARTED</a>
</div>
<div class="abs dots"><i></i><i class="on"></i><i></i></div>

<h2 class="abs section-title" style="top:834px">SERVICES</h2>

<div class="abs service" style="left:137px;top:943px"><div class="ring"><div class="photo" role="img" aria-label="Hands typing on a laptop at a desk" style="background:radial-gradient(circle at 30% 25%,#f6c27a 0,rgba(246,194,122,0) 40%),radial-gradient(circle at 55% 65%,#e9d2c0 0,rgba(233,210,192,0) 35%),linear-gradient(160deg,#d9823a,#b2582a 50%,#5a3b2c)"></div></div><h3>STOCK WORK</h3></div>
<div class="abs service" style="left:449px;top:943px"><div class="ring"><div class="photo" role="img" aria-label="Spraying work in progress" style="background:radial-gradient(circle at 30% 20%,#f0c590 0,rgba(240,197,144,0) 40%),linear-gradient(135deg,#c8672a,#e8d3bd 55%,#a5542a)"></div></div><h3>SPRAYING</h3></div>
<div class="abs service" style="left:761px;top:943px"><div class="ring"><div class="photo" role="img" aria-label="Green pasture with hills and a fence line" style="background:linear-gradient(180deg,#aac6dc 0,#e4ebee 38%,#8ea06a 46%,#6f8f3c 52%,#7f9c3a 70%,#5b7d26 100%)"></div></div><h3>PASTURES</h3></div>
<div class="abs spray-overlay"><strong>SPRAYING</strong><span>Spraying weeds<br>Spraying gorse</span></div>

<div class="abs service" style="left:137px;top:1318px"><div class="ring"><div class="photo" role="img" aria-label="Glass towers seen from below against a blue sky" style="background:radial-gradient(circle at 45% 55%,#e6f3fb 0,rgba(230,243,251,0) 35%),linear-gradient(135deg,#2f6aa6,#6fb1e0 45%,#2a5f96 75%,#163d66)"></div></div><h3>BUILDING</h3></div>
<div class="abs service" style="left:449px;top:1318px"><div class="ring"><div class="photo" role="img" aria-label="Black metal fence in a green garden" style="background:radial-gradient(circle at 30% 25%,#c7d98c 0,rgba(199,217,140,0) 40%),linear-gradient(160deg,#7fa043,#3f5a1c 50%,#1c2614 75%,#9aa956)"></div></div><h3>FENCING</h3></div>
<div class="abs service" style="left:761px;top:1318px"><div class="ring"><div class="photo" role="img" aria-label="Water management icons in front of a person in a suit" style="background:radial-gradient(circle at 35% 50%,#8fb0c8 0,rgba(143,176,200,0) 45%),radial-gradient(circle at 75% 40%,#2fa7c9 0,rgba(47,167,201,0) 20%),linear-gradient(135deg,#a8bccd,#55728d 50%,#23374a)"></div></div><h3>WATER<br>MANAGEMENT</h3></div>

<a class="abs btn btn-green" style="left:526px;top:1703px">VIEW MORE</a>

<svg class="abs" style="left:0;top:1815px" width="1200" height="565" viewBox="0 1815 1200 565">
  <defs>
    <clipPath id="aboutClip"><ellipse cx="600" cy="2096" rx="594" ry="275"/></clipPath>
    <linearGradient id="aboutBg" x1="0" y1="0" x2="0" y2="1">
      <stop offset="0" stop-color="#5c9a16"/>
      <stop offset=".45" stop-color="#7cb52a"/>
      <stop offset=".7" stop-color="#5f9a1a"/>
      <stop offset="1" stop-color="#4a8210"/>
    </linearGradient>
    <radialGradient id="aboutGlow" cx=".5" cy=".5" r=".5">
      <stop offset="0" stop-color="#a6d65a" stop-opacity=".8"/>
      <stop offset="1" stop-color="#a6d65a" stop-opacity="0"/>
    </radialGradient>
  </defs>
  <g clip-path="url(#aboutClip)" role="img" aria-label="Green field with a flowing stream">
    <rect x="0" y="1815" width="1200" height="565" fill="url(#aboutBg)"/>
    <ellipse cx="900" cy="1960" rx="320" ry="120" fill="url(#aboutGlow)"/>
    <ellipse cx="780" cy="2230" rx="380" ry="90" fill="url(#aboutGlow)" opacity=".6"/>
  </g>
</svg>
<div class="abs about-photo" role="img" aria-label="Worker in a safety vest beside tall steel panels" style="background:radial-gradient(ellipse at 55% 55%,#d96a2a 0,rgba(217,106,42,0) 12%),linear-gradient(90deg,#a9bccb,#6f8799 35%,#2b3540 55%,#8ea4b6 80%,#5f7587)"></div>
<div class="abs about-copy">
  <h2>ABOUT US</h2>
  <p>Sed ut perspiciatis unde omnis iste natus error sit voluptatem accusantium doloremque laudantium, totam rem aperiam, eaque ipsa quae ab illo inventore veritatis et quasi architecto beatae vitae dicta sunt explicabo. Nemo enim ipsam voluptatem quia voluptas sit aspernatur aut odit aut fugit, sed quia consequuntur magni dolores eos qui ratione voluptatem sequi nesciunt. Neque porro quisquam est, qui dolorem ipsum quia dolor sit amet, consectetur, adipisci velit, sed quia non numquam eius modi tempora incidunt ut labore et dolore magnam aliquam quaerat voluptatem.</p>
  <a class="btn btn-black">READ MORE</a>
</div>

<h2 class="abs section-title" style="top:2455px">GALLERY</h2>
<div class="abs gallery">
  <div role="img" aria-label="Steel pipeline across green hills at sunset" style="background:radial-gradient(ellipse at 40% 55%,#d8a85a 0,rgba(216,168,90,0) 35%),linear-gradient(180deg,#8ea7bd 0,#c9b68e 30%,#3f5f86 48%,#6e8c3a 70%,#4c6a22)"></div>
  <div role="img" aria-label="Laptop showing a financial chart" style="background:radial-gradient(ellipse at 45% 50%,#e07a5c 0,rgba(224,122,92,0) 30%),linear-gradient(160deg,#2c2a2c,#4a3e3c 45%,#c9ad8a 75%,#e4d1b6)"></div>
  <div role="img" aria-label="Open green meadow under a blue sky" style="background:linear-gradient(180deg,#7fa8cf 0,#d6e4ec 40%,#4f7a24 50%,#7eab32 70%,#5e8d22)"></div>
  <div role="img" aria-label="Person studying computer screens" style="background:radial-gradient(ellipse at 30% 40%,#3f8fc2 0,rgba(63,143,194,0) 30%),radial-gradient(ellipse at 15% 15%,#c7522e 0,rgba(199,82,46,0) 18%),linear-gradient(135deg,#14202c,#2a3e52 50%,#0e141a)"></div>
  <div role="img" aria-label="Garden lawn with a timber fence and trees" style="background:linear-gradient(180deg,#dfe5e8 0,#6e943a 25%,#4e7428 40%,#9a7452 50%,#7e5c3e 62%,#6a9a34 72%,#4f7e22)"></div>
  <div role="img" aria-label="Apartment building against a blue sky" style="background:radial-gradient(ellipse at 70% 60%,#d39a66 0,rgba(211,154,102,0) 40%),linear-gradient(135deg,#2f6fc0,#7ab0e2 45%,#c8875a 70%,#8a5a3a)"></div>
</div>
<div class="abs zoom"><svg width="16" height="16" viewBox="0 0 16 16"><circle cx="7" cy="7" r="4.5" fill="none" stroke="#fff" stroke-width="2"/><path d="M10.5 10.5l3.5 3.5" stroke="#fff" stroke-width="2" stroke-linecap="round"/></svg></div>

<a class="abs btn btn-green" style="left:526px;top:3124px">VIEW MORE</a>

<svg class="abs" style="left:0;top:3230px" width="1200" height="660" viewBox="0 3230 1200 660">
  <defs>
    <clipPath id="contactClip"><ellipse cx="600" cy="3553" rx="586" ry="313"/></clipPath>
    <radialGradient id="contactBg" cx=".5" cy=".8" r=".75">
      <stop offset="0" stop-color="#7a7a7a"/>
      <stop offset=".4" stop-color="#333"/>
      <stop offset="1" stop-color="#0b0b0b"/>
    </radialGradient>
    <radialGradient id="ripple" cx=".5" cy=".5" r=".5">
      <stop offset="0" stop-color="#9a9a9a" stop-opacity="0"/>
      <stop offset=".8" stop-color="#9a9a9a" stop-opacity=".25"/>
      <stop offset="1" stop-color="#9a9a9a" stop-opacity="0"/>
    </radialGradient>
  </defs>
  <ellipse cx="608" cy="3561" rx="588" ry="315" fill="var(--green)"/>
  <g clip-path="url(#contactClip)" role="img" aria-label="Dark water surface with ripples">
    <rect x="0" y="3230" width="1200" height="660" fill="url(#contactBg)"/>
    <ellipse cx="600" cy="3790" rx="520" ry="110" fill="url(#ripple)"/>
    <ellipse cx="600" cy="3790" rx="330" ry="65" fill="url(#ripple)"/>
  </g>
</svg>
<h2 class="abs section-title contact-title">CONTACT US</h2>
<div class="abs field" style="left:173px;top:3492px;width:276px;height:44px">Enter Name</div>
<div class="abs field" style="left:462px;top:3492px;width:276px;height:44px">Enter Email</div>
<div class="abs field" style="left:751px;top:3492px;width:276px;height:44px">Phone</div>
<div class="abs field msg" style="left:173px;top:3551px;width:854px;height:86px">Message</div>
<a class="abs btn btn-green" style="left:502px;top:3655px;width:196px;height:55px">SUBMIT MESSGAE</a>

<a class="abs brand footer-brand"><span class="mark"></span><span class="name">TIDY FERN<small>SERVICES</small></span></a>
<nav class="abs nav footer-nav">
  <a style="left:0">HOME</a>
  <a style="left:80px">ABOUT US</a>
  <a style="left:187px">SERVICES</a>
  <a style="left:291px">GALLERY</a>
  <a style="left:389px">CONTACT US</a>
</nav>
<p class="abs copyright">© 2024 Tidy fern Services. All rights reserved.Privacy | Terms of Use</p>
<div class="abs socials" aria-label="Social links"><i></i><i></i><i></i><i></i><i></i></div>
</body>
</html>
```